Bourbon label design for bourbon brand. Looking to freshen our current label.

I need a Bourbon label design for our rebranded Bourbon bottle. Label should include picture of our horse and our logo on the bottle. Front Label is 3.5 inches wide and 6 inches tall, back label is 4 inches tall and 3 inches wide. Back label can be a simple plain logo like the one in the brief. I have included a design of our current bottle and label. We want to stay close to the current color schemes but want a fresh rebrand of the design. The label needs to be the correct size on a tall bottle like pictured.

Target Market(s)

Our Bourbon members, 30-50 year old males

Requirements
Must have
• Picture of our horse, our B logo , straight Bourbon whiskey on the front. Room to edit text on the back label.

```html
<!DOCTYPE html>
<html lang="en">
<head>
<meta charset="utf-8">
<title>Nightfall Straight Bourbon Whiskey – Front Label</title>
<link rel="stylesheet" href="https://fonts.googleapis.com/css2?family=Rye&family=Smokum&display=swap">
<style>
  :root {
    --backdrop-light: #f3e6b8;
    --backdrop-dark: #cdb57f;
    --label-black: #000000;
    --gold: #c9a45c;
    --silver: #e6e6e6;
    --white: #ffffff;
    --art-light: #9a9a9a;
    --art-dark: #1a1a1a;
  }
  * { margin: 0; padding: 0; box-sizing: border-box; }
  html, body {
    width: 1200px; height: 1200px; overflow: hidden;
  }
  body {
    background: radial-gradient(ellipse at 50% 45%, var(--backdrop-light) 0%, var(--backdrop-dark) 100%);
    position: relative;
  }
  .front-label {
    position: absolute;
    left: 237px; top: 55px;
    width: 726px; height: 1089px;
    background: var(--label-black);
    color: var(--silver);
    font-family: "Smokum", "Rye", serif;
  }
  .label-header {
    position: absolute;
    top: 44px; left: 0; width: 100%;
    display: flex; align-items: center; justify-content: center; gap: 18px;
  }
  .header-rules { width: 190px; height: 28px; }
  .label-header .edition {
    font-size: 50px; letter-spacing: 3px; color: var(--silver);
  }
  .horse-artwork {
    position: absolute;
    left: 110px; top: 120px;
    width: 506px; height: 760px;
    border-radius: 48% 48% 42% 42%;
    background: radial-gradient(ellipse at 50% 40%, var(--art-light) 0%, #4a4a4a 45%, var(--art-dark) 80%, var(--label-black) 100%);
  }
  .brand-mark {
    position: absolute;
    top: 500px; left: 0; width: 100%;
    display: flex; justify-content: center;
  }
  .brand-mark .mark-circle {
    width: 96px; height: 96px; border-radius: 50%;
    background: var(--white);
  }
  .brand-name {
    position: absolute;
    top: 600px; left: 0; width: 100%;
    text-align: center;
    font-family: "Rye", serif;
    font-size: 96px; line-height: 1;
    color: var(--silver);
    letter-spacing: 2px;
  }
  .product-type {
    position: absolute;
    top: 712px; left: 0; width: 100%;
    text-align: center;
    font-size: 42px; letter-spacing: 1px;
    color: var(--gold);
  }
  .spec { position: absolute; text-align: center; line-height: 1; }
  .spec .value { display: block; font-size: 50px; color: var(--silver); }
  .spec .unit { display: block; font-size: 26px; color: var(--silver); margin-top: 4px; }
  .spec-abv { left: 72px; top: 790px; }
  .spec-age { right: 90px; top: 790px; }
  .cask-note {
    position: absolute;
    font-size: 44px; line-height: 0.95;
    color: var(--gold); text-align: center;
  }
  .cask-single { left: 64px; top: 910px; }
  .cask-strength { right: 50px; top: 910px; }
  .volume {
    position: absolute;
    top: 1010px; left: 0; width: 100%;
    text-align: center;
    font-size: 30px; color: var(--silver); letter-spacing: 1px;
  }
</style>
</head>
<body>
  <section class="front-label">
    <header class="label-header">
      <svg class="header-rules" viewBox="0 0 190 28" aria-hidden="true">
        <line x1="0" y1="5" x2="190" y2="5" stroke="#c9a45c" stroke-width="2"/>
        <line x1="0" y1="14" x2="190" y2="14" stroke="#c9a45c" stroke-width="2"/>
        <line x1="0" y1="23" x2="190" y2="23" stroke="#c9a45c" stroke-width="2"/>
      </svg>
      <span class="edition">SPECIAL</span>
      <svg class="header-rules" viewBox="0 0 190 28" aria-hidden="true">
        <line x1="0" y1="5" x2="190" y2="5" stroke="#c9a45c" stroke-width="2"/>
        <line x1="0" y1="14" x2="190" y2="14" stroke="#c9a45c" stroke-width="2"/>
        <line x1="0" y1="23" x2="190" y2="23" stroke="#c9a45c" stroke-width="2"/>
      </svg>
    </header>

    <div class="horse-artwork" role="img" aria-label="Black and white splatter illustration of the brand's racehorse with jockey charging forward"></div>

    <div class="brand-mark"><span class="mark-circle"></span></div>
    <h1 class="brand-name">NIGHTFALL</h1>
    <p class="product-type">STRAIGHT BOURBON WHISKEY</p>

    <div class="spec spec-abv"><span class="value">66%</span><span class="unit">ALC/ VOL</span></div>
    <div class="spec spec-age"><span class="value">12</span><span class="unit">YEARS</span></div>

    <p class="cask-note cask-single">SINGLE<br>BARREL</p>
    <p class="cask-note cask-strength">BARREL<br>STRAIGHT</p>

    <p class="volume">750 ML</p>
  </section>
</body>
</html>
```